Social shared calender for Parents

I need an app design to create groups to share common calender events for mothers (whose children are in school) like meetings, bday parties, play groups, assignments.
Simple design with overlapping colour coded activities which can be displayed in a day, month format with a downloaded school calender

I can create private or shared events on my calender app. Also subscribe to other calenders if needed

Target Market(s)

Mothers/Parents around their 30s

Industry/Entity Type

Events

Requirements
Must have
• Colourful/Bold and simple to use.

```html
<!DOCTYPE html>
<html lang="en">
<head>
<meta charset="utf-8">
<title>Social Calendar Mobile Visual Designs</title>
<link href="https://fonts.googleapis.com/css2?family=Open+Sans:wght@400&family=Quicksand:wght@400;500;600;700&display=swap" rel="stylesheet">
<style>
:root{
  --page:#e6e9ee;
  --screen:#ffffff;
  --ink:#222428;
  --muted:#8d9096;
  --heading:#4a4f58;
  --rule:#e4e6ea;
  --button:#0b77b7;
  --accent:#1a8fd6;
  --day-blue:#14a8de;
  --day-orange:#f0901c;
  --badge-yellow:#f5bd1f;
  --count-blue:#1ba7e2;
}
*{box-sizing:border-box;margin:0;padding:0}
html,body{width:1200px;height:1000px;overflow:hidden;background:var(--page)}
body{position:relative;font-family:"Quicksand",sans-serif;color:var(--ink)}
.page-title{position:absolute;left:65px;top:140px;font-family:"Open Sans",sans-serif;font-size:24px;color:var(--heading);letter-spacing:.3px}
.screen-label{position:absolute;top:286px;font-family:"Open Sans",sans-serif;font-size:20px;color:var(--heading)}
.screen{position:absolute;top:335px;width:227px;height:402px;background:var(--screen);box-shadow:0 18px 30px rgba(60,70,90,.18)}
.topbar{position:absolute;left:0;right:0;top:0;height:38px;border-bottom:1px solid var(--rule);display:flex;align-items:center;justify-content:center;font-size:11px;font-weight:500;letter-spacing:.4px}
.topbar .back{position:absolute;left:9px;top:13px}
.topbar .add{position:absolute;right:9px;top:12px}
.tabbar{position:absolute;left:0;right:0;bottom:0;height:45px;border-top:1px solid var(--rule);display:flex;justify-content:space-around;padding:0 4px}
.tab{display:flex;flex-direction:column;align-items:center;width:54px;padding-top:6px;font-size:6px;font-weight:700;letter-spacing:.2px;color:var(--ink)}
.tab svg{width:18px;height:16px;margin-bottom:3px;stroke:currentColor;fill:none;stroke-width:1.2}
.tab.active{color:var(--accent)}
/* home */
.month-title{position:absolute;top:53px;width:100%;text-align:center;font-weight:700;font-size:13px;letter-spacing:.3px}
.calendar{position:absolute;left:17px;top:82px;display:grid;grid-template-columns:repeat(7,27.5px);grid-auto-rows:36px;font-size:10px;font-weight:600}
.day{position:relative;display:flex;align-items:center;justify-content:center}
.day.marked span{width:17px;height:17px;border-radius:50%;color:#fff;display:flex;align-items:center;justify-content:center}
.day.blue span{background:var(--day-blue)}
.day.orange span{background:var(--day-orange)}
.day .badge{position:absolute;left:50%;top:4px;margin-left:3px;width:10px;height:10px;border-radius:50%;background:var(--badge-yellow);color:#fff;font-size:6px;display:flex;align-items:center;justify-content:center}
.events-rule{position:absolute;left:0;right:0;top:265px;border-top:1px solid var(--rule)}
.events-title{position:absolute;top:272px;width:100%;text-align:center;font-weight:700;font-size:10px;letter-spacing:.2px}
.event-row{position:absolute;top:294px;left:26px;font-size:8px;font-weight:500}
.event-row .time{display:inline-block;width:50px}
/* form */
.field{position:absolute;left:0;width:100%;text-align:center}
.field-label{font-size:7.5px;font-weight:700;letter-spacing:.3px}
.field-value{margin-top:7px;font-size:12px;color:var(--muted);letter-spacing:.3px}
.field-value svg{margin-left:6px;vertical-align:middle}
.primary-button{position:absolute;left:8px;right:8px;height:27px;border-radius:3px;background:var(--button);color:#fff;font-size:8px;font-weight:700;letter-spacing:.4px;display:flex;align-items:center;justify-content:center}
/* account */
.avatar{position:absolute;border-radius:50%}
.photo-warm{background:radial-gradient(circle at 50% 45%,#c89a7f 0%,#8a5a43 55%,#b9b3ac 100%)}
.account-field{position:absolute;left:25px;font-size:9px;font-weight:500;letter-spacing:.4px;color:#3b3e44}
/* friends */
.friend{position:absolute;left:0;width:100%;height:56px}
.friend .avatar{left:14px;top:0;width:55px;height:55px}
.friend-name{position:absolute;left:80px;top:15px;font-size:9px;font-weight:500;letter-spacing:.4px}
.friend-count{display:inline-flex;width:13px;height:13px;border-radius:50%;background:var(--count-blue);color:#fff;font-size:7px;font-weight:700;align-items:center;justify-content:center;margin-left:4px;vertical-align:middle}
.friend-group{position:absolute;left:80px;top:32px;font-size:5.5px;font-weight:700;letter-spacing:.2px}
</style>
</head>
<body>
<svg width="0" height="0" style="position:absolute">
  <defs>
    <symbol id="i-home" viewBox="0 0 18 16"><path d="M2 8 9 1.5 16 8M4 6.5V15h4v-4h2v4h4V6.5"/></symbol>
    <symbol id="i-friends" viewBox="0 0 26 16"><circle cx="6" cy="5" r="2.6"/><circle cx="13" cy="5" r="2.6"/><circle cx="20" cy="5" r="2.6"/><path d="M1.5 14c0-3 2-5 4.5-5s4.5 2 4.5 5M8.5 14c0-3 2-5 4.5-5s4.5 2 4.5 5M15.5 14c0-3 2-5 4.5-5s4.5 2 4.5 5"/></symbol>
    <symbol id="i-groups" viewBox="0 0 18 16"><circle cx="9" cy="8" r="6.5"/><circle cx="6" cy="8" r=".6" fill="currentColor"/><circle cx="9" cy="8" r=".6" fill="currentColor"/><circle cx="12" cy="8" r=".6" fill="currentColor"/></symbol>
    <symbol id="i-account" viewBox="0 0 18 16"><circle cx="9" cy="5" r="3.8"/><path d="M2 15.5c0-4 3-6.5 7-6.5s7 2.5 7 6.5z"/></symbol>
    <symbol id="i-back" viewBox="0 0 8 10"><path d="M6 1 2 5l4 4" fill="none" stroke="#222" stroke-width="1.6"/></symbol>
    <symbol id="i-add" viewBox="0 0 12 12"><path d="M6 0v12M0 6h12" stroke="#222" stroke-width="1.3"/></symbol>
  </defs>
</svg>

<h1 class="page-title">SOCIAL CALENDAR MOBILE VISUAL DESIGNS</h1>

<div class="screen-label" style="left:61px">1.0 Home</div>
<div class="screen-label" style="left:343px">2.0 Create New Event</div>
<div class="screen-label" style="left:626px">3.0 My Account</div>
<div class="screen-label" style="left:913px">3.1 Friends</div>

<!-- Home -->
<section class="screen screen-home" style="left:61px">
  <header class="topbar"><svg class="back" width="8" height="10"><use href="#i-back"/></svg>HOME<svg class="add" width="12" height="12"><use href="#i-add"/></svg></header>
  <div class="month-title">19 JANUARY 2014</div>
  <div class="calendar">
    <div class="day">1</div><div class="day">2</div><div class="day">3</div><div class="day">4</div><div class="day">5</div><div class="day">6</div><div class="day">7</div>
    <div class="day">8</div><div class="day">9</div><div class="day">10</div><div class="day">11</div><div class="day">12</div><div class="day">13</div><div class="day">14</div>
    <div class="day">15</div><div class="day">16</div><div class="day">17</div>
    <div class="day marked blue"><span>18</span><i class="badge">2</i></div>
    <div class="day marked orange"><span>19</span><i class="badge">1</i></div>
    <div class="day">20</div><div class="day">21</div>
    <div class="day">22</div>
    <div class="day marked blue"><span>23</span><i class="badge">1</i></div>
    <div class="day">24</div><div class="day">25</div><div class="day">26</div><div class="day">27</div><div class="day">28</div>
    <div class="day">29</div><div class="day">30</div><div class="day">31</div>
  </div>
  <div class="events-rule"></div>
  <div class="events-title">TODAY'S EVENTS</div>
  <div class="event-row"><span class="time">7:00 PM</span>Mia's birthday</div>
  <nav class="tabbar">
    <div class="tab active"><svg><use href="#i-home"/></svg>HOME</div>
    <div class="tab"><svg style="width:26px"><use href="#i-friends"/></svg>FRIENDS</div>
    <div class="tab"><svg><use href="#i-groups"/></svg>GROUPS</div>
    <div class="tab"><svg><use href="#i-account"/></svg>MY ACCOUNT</div>
  </nav>
</section>

<!-- Create new event -->
<section class="screen screen-create" style="left:341px">
  <header class="topbar"><svg class="back" width="8" height="10"><use href="#i-back"/></svg>CREATE NEW EVENT</header>
  <div class="field" style="top:49px"><div class="field-label">EVENT *</div><div class="field-value">name of the event</div></div>
  <div class="field" style="top:98px"><div class="field-label">DATE *</div><div class="field-value">00 - 00 - 0000</div></div>
  <div class="field" style="top:153px"><div class="field-label">TIME *</div><div class="field-value">00 - 00 - 00 - AM</div></div>
  <div class="field" style="top:206px"><div class="field-label">GROUP</div><div class="field-value">select from groups<svg width="8" height="5"><path d="M1 1l3 3 3-3" fill="none" stroke="#555" stroke-width="1"/></svg></div></div>
  <div class="field" style="top:264px"><div class="field-label">FRIENDS</div><div class="field-value">select from events<svg width="8" height="5"><path d="M1 1l3 3 3-3" fill="none" stroke="#555" stroke-width="1"/></svg></div></div>
  <div class="primary-button" style="top:317px">CREATE EVENT</div>
  <nav class="tabbar">
    <div class="tab"><svg><use href="#i-home"/></svg>HOME</div>
    <div class="tab"><svg style="width:26px"><use href="#i-friends"/></svg>FRIENDS</div>
    <div class="tab"><svg><use href="#i-groups"/></svg>GROUPS</div>
    <div class="tab"><svg><use href="#i-account"/></svg>MY ACCOUNT</div>
  </nav>
</section>

<!-- My account -->
<section class="screen screen-account" style="left:624px">
  <header class="topbar"><svg class="back" width="8" height="10"><use href="#i-back"/></svg>MY ACCOUNT<svg class="add" width="12" height="12"><use href="#i-add"/></svg></header>
  <div class="avatar photo-warm" role="img" aria-label="Profile photo of the account holder" style="left:69px;top:53px;width:90px;height:90px"></div>
  <div class="account-field" style="top:169px">YOUR NAME</div>
  <div class="account-field" style="top:204px">EMAIL</div>
  <div class="account-field" style="top:240px">PASSWORD</div>
  <div class="account-field" style="top:275px">CONFIRM PASSWORD</div>
  <div class="primary-button" style="top:311px">EDIT ACCOUNT</div>
  <nav class="tabbar">
    <div class="tab"><svg><use href="#i-home"/></svg>HOME</div>
    <div class="tab"><svg style="width:26px"><use href="#i-friends"/></svg>FRIENDS</div>
    <div class="tab"><svg><use href="#i-groups"/></svg>GROUPS</div>
    <div class="tab active"><svg><use href="#i-account"/></svg>MY ACCOUNT</div>
  </nav>
</section>

<!-- Friends -->
<section class="screen screen-friends" style="left:911px">
  <header class="topbar"><svg class="back" width="8" height="10"><use href="#i-back"/></svg>FRIENDS<svg class="add" width="12" height="12"><use href="#i-add"/></svg></header>
  <div class="friend" style="top:53px">
    <div class="avatar photo-warm" role="img" aria-label="Profile photo of Nora Bell"></div>
    <div class="friend-name">NORA BELL<span class="friend-count">2</span></div>
    <div class="friend-group">SCHOOL</div>
  </div>
  <div class="friend" style="top:122px">
    <div class="avatar photo-warm" role="img" aria-label="Profile photo of Clara Hayes"></div>
    <div class="friend-name">CLARA HAYES<span class="friend-count">1</span></div>
    <div class="friend-group">SCHOOL</div>
  </div>
  <div class="friend" style="top:191px">
    <div class="avatar photo-warm" role="img" aria-label="Profile photo of Jenna Moore"></div>
    <div class="friend-name">JENNA MOORE<span class="friend-count">2</span></div>
    <div class="friend-group">NEIGHBORS</div>
  </div>
  <div class="friend" style="top:260px">
    <div class="avatar photo-warm" role="img" aria-label="Profile photo of Laura Price"></div>
    <div class="friend-name">LAURA PRICE<span class="friend-count">3</span></div>
    <div class="friend-group">OFFICE</div>
  </div>
  <nav class="tabbar">
    <div class="tab"><svg><use href="#i-home"/></svg>HOME</div>
    <div class="tab active"><svg style="width:26px"><use href="#i-friends"/></svg>FRIENDS</div>
    <div class="tab"><svg><use href="#i-groups"/></svg>GROUPS</div>
    <div class="tab"><svg><use href="#i-account"/></svg>MY ACCOUNT</div>
  </nav>
</section>
</body>
</html>
```